Extra job from Miami Logo design job

This posting is for the winner of the Lorvane Swim Shop logo, we need an example of what the commerce webpage would look like.

Please go here to submit the logo first:

http://jobs.pixelmarquee.com/job.aspx?id=512807.

Shop

```html
<!DOCTYPE html>
<html lang="en">
<head>
<meta charset="utf-8">
<title>Lorvane Swim Shop – Storefront</title>
<link href="https://fonts.googleapis.com/css2?family=Open+Sans:wght@400;600;700;800&display=swap" rel="stylesheet">
<style>
:root{
  --coral:#f76565;
  --coral-dark:#e95252;
  --page:#ececec;
  --white:#ffffff;
  --ink:#333333;
  --muted:#8c8c8c;
  --dark:#2b2b2b;
  --darker:#232323;
  --panel:#3a3a3a;
  --teal:#4bb3d6;
  --green:#7cc243;
  --star:#f5b400;
}
*{box-sizing:border-box;margin:0;padding:0}
html,body{width:1200px;height:1000px;overflow:hidden}
body{background:var(--page);font-family:"Open Sans",Arial,sans-serif;color:var(--ink);position:relative;font-size:6px}
.abs{position:absolute}
.wide{transform-origin:left top;white-space:nowrap}
.topbar{left:0;top:0;width:1200px;height:12px;background:#f6f6f6;border-bottom:1px solid #dcdcdc}
.topbar-links{right:150px;top:1px;display:flex;gap:14px;font-size:6px;color:var(--muted)}
.topbar-links span::before{content:"";display:inline-block;width:5px;height:5px;background:#bbb;margin-right:3px;vertical-align:middle}
.brand{left:150px;top:16px;display:flex;align-items:center;gap:6px;font-size:19px;font-weight:700;color:var(--coral);line-height:22px;white-space:nowrap}
.brand i{width:14px;height:14px;background:var(--coral);border-radius:50%;display:block}
.perks{left:392px;top:18px;display:flex;gap:28px}
.perk{display:flex;gap:6px;align-items:center;font-size:6px;color:var(--muted);line-height:7px}
.perk i{width:16px;height:10px;background:#cfcfcf;border-radius:2px;display:block}
.perk b{font-weight:600;color:#777;display:block}
.cart-btn{left:928px;top:21px;width:118px;height:12px;background:var(--coral);border-radius:6px;color:#fff;font-size:6px;line-height:12px;text-align:center}
.nav{left:150px;top:41px;width:896px;height:14px;background:var(--coral)}
.nav ul{list-style:none;display:flex;gap:34px;padding-left:18px;font-size:6px;font-weight:700;color:#fff;line-height:14px}
.search{right:6px;top:2px;width:200px;height:10px;background:#fff;border-radius:2px;font-size:6px;color:#aaa;line-height:10px;padding-left:5px}
.ph{display:block}
.slider{left:150px;top:59px;width:896px;height:130px;background:linear-gradient(100deg,#c9a27f 0%,#d6c0a3 35%,#8fb2bf 60%,#a9c3cc 100%)}
.slider-title{left:565px;top:82px;font-size:30px;font-weight:800;color:var(--coral);letter-spacing:1px;transform:scaleX(1.8)}
.slider-sub{left:563px;top:110px;font-size:12px;font-weight:700;color:#111;line-height:14px;transform:scaleX(1.4)}
.arrow-btn{width:46px;height:16px}
.brands{left:150px;top:194px;width:896px;height:22px;background:#fff;display:flex;align-items:center;justify-content:space-around;padding:0 40px;font-size:12px;font-weight:700;color:#222}
.brands-arrow{top:199px;font-size:10px;color:#aaa}
.tile{position:absolute}
.tab{height:11px;padding:0 10px;background:var(--coral);color:#fff;font-size:6px;font-weight:700;line-height:11px;border-radius:2px 2px 0 0}
.pager{width:30px;height:6px;display:flex;gap:2px}
.pager i{flex:1;background:#fff;border:1px solid #ddd}
.card{position:absolute;background:#fff;width:214px}
.card .img{height:72px}
.meta{padding:4px 6px;font-size:5px;color:var(--muted);line-height:7px}
.stars{color:var(--star);letter-spacing:1px;margin-right:4px}
.price{color:var(--coral);font-weight:700;font-size:9px;line-height:11px}
.price s{color:#aaa;font-size:5px;font-weight:400;margin-left:3px}
.desc{color:#333;font-size:5px;font-weight:600;text-transform:uppercase}
.ribbon{position:absolute;top:0;right:0;width:0;height:0;border-top:18px solid var(--green);border-left:38px solid transparent}
.promo{left:150px;top:442px;width:896px;height:33px;background:linear-gradient(90deg,#1d1d1d,#333 60%,#555)}
.promo-name{left:337px;top:445px;font-size:13px;font-weight:800;color:#fff;letter-spacing:2px}
.promo-sub{left:337px;top:460px;font-size:7px;font-weight:600;color:#ddd;letter-spacing:1px}
.cats{left:150px;top:482px;width:215px;height:98px;background:var(--panel)}
.cats-head{height:10px;background:var(--teal);color:#fff;font-size:6px;font-weight:700;line-height:10px;padding-left:6px}
.cats ul{list-style:none}
.cats li{height:14.6px;border-bottom:1px solid #4a4a4a;color:#ddd;font-size:6px;line-height:14px;padding-left:18px;position:relative}
.cats li.plus::after{content:"+";position:absolute;right:16px;top:3px;width:8px;height:8px;border-radius:50%;background:#555;font-size:6px;line-height:8px;text-align:center}
.side-banner{left:150px;top:584px;width:215px;height:109px;background:linear-gradient(135deg,#6b5a4e,#c9b9aa 60%,#e9e9e9)}
.side-title{left:172px;top:655px;font-size:13px;font-weight:800;color:#4fb83a;transform:scaleX(1.8)}
.side-sub{left:175px;top:670px;font-size:10px;font-weight:700;color:#222;transform:scaleX(1.6)}
.wide-banner{left:150px;top:727px;width:896px;height:38px;background:linear-gradient(90deg,#b58f72,#6aa5c2 40%,#8ec1d6 70%,#d7bda2)}
.wide-title{left:466px;top:729px;font-size:20px;font-weight:800;color:#111;letter-spacing:1px;transform:scaleX(2.05)}
.wide-sub{left:398px;top:751px;font-size:10px;font-weight:700;color:#fff;letter-spacing:.5px;transform:scaleX(1.5)}
.services{left:150px;top:772px;width:896px;height:28px;background:#fff;display:flex;padding:7px 18px}
.service{flex:1;display:flex;gap:10px}
.service i{width:18px;height:12px;border-radius:2px;display:block;margin-top:2px}
.service b{display:block;font-size:6px;font-weight:800;line-height:7px}
.service span{font-size:5px;color:#aaa;line-height:6px;display:block}
.footer{left:150px;top:805px;width:896px;height:163px;background:var(--dark)}
.fcol{position:absolute;color:#999;font-size:5px;line-height:7.5px}
.fcol h4{color:#fff;font-size:6px;font-weight:700;margin-bottom:4px}
.fline{display:flex;gap:5px;align-items:center;margin-top:4px}
.fline i{width:10px;height:6px;border-radius:3px;background:#666;display:block}
.tweet{display:flex;gap:4px;margin-bottom:5px}
.tweet i{width:10px;height:10px;background:#e98e3a;border-radius:2px;flex:none}
.tweet em{color:var(--coral);font-style:normal}
.blog{display:flex;gap:6px;margin-bottom:4px}
.blog i{width:24px;height:12px;background:#5b4c46;flex:none}
.blog em{color:var(--coral);font-style:normal;font-weight:600}
.email{width:110px;height:11px;background:#fff;color:#999;font-size:5px;line-height:11px;padding-left:4px}
.subscribe{width:48px;height:11px;background:var(--coral);color:#fff;font-size:6px;line-height:11px;text-align:center}
.social{display:flex;gap:6px;margin-top:3px}
.social i{width:22px;height:9px;background:#444;display:block}
.bottom{left:150px;top:968px;width:896px;height:22px;background:var(--darker);color:#888;font-size:5px;line-height:7px;padding:3px 16px}
.bottom em{color:var(--coral);font-style:normal}
.pay{right:16px;top:7px;display:flex;gap:8px;font-size:6px;font-weight:700;color:#4a8fd0}
</style>
</head>
<body>
<div class="abs topbar"></div>
<div class="abs topbar-links"><span>Wish List (0)</span><span>My Account</span><span>Shopping Cart</span><span>Checkout</span><span>Setting</span></div>

<header>
  <div class="abs brand"><i></i>Lorvane Swim Shop</div>
  <div class="abs perks">
    <div class="perk"><i></i><div><b>Free shipping</b>On All Products</div></div>
    <div class="perk"><i></i><div><b>Money back</b>Guarantee</div></div>
    <div class="perk"><i></i><div><b>Special weekly</b>Offer</div></div>
  </div>
  <div class="abs cart-btn">0 item(s) - $0.00</div>
  <nav class="abs nav">
    <ul><li>HOME</li><li>BLOGS</li><li>CONTACTS US</li></ul>
    <div class="abs search">Search...</div>
  </nav>
</header>

<main>
  <div class="abs slider ph" role="img" aria-label="Beach photo of a model in a striped bikini"></div>
  <div class="abs slider-title wide">LOREM IPSUM</div>
  <div class="abs slider-sub wide">dummy text of the printing and<br>typesetting industry.</div>
  <svg class="abs arrow-btn" style="left:173px;top:120px" viewBox="0 0 46 16"><rect width="46" height="16" rx="2" fill="#222"/><path d="M25 4l-4 4 4 4" stroke="#fff" stroke-width="2" fill="none"/></svg>
  <svg class="abs arrow-btn" style="left:975px;top:120px" viewBox="0 0 46 16"><rect width="46" height="16" rx="2" fill="#222"/><path d="M21 4l4 4-4 4" stroke="#fff" stroke-width="2" fill="none"/></svg>

  <div class="abs brands"><span>Brightloop</span><span>Brightloop</span><span>Brightloop</span><span>Brightloop</span><span>Brightloop</span><span>Brightloop</span></div>
  <div class="abs brands-arrow" style="left:170px">‹</div>
  <div class="abs brands-arrow" style="left:1020px">›</div>

  <div class="tile ph" style="left:150px;top:221px;width:298px;height:42px;background:linear-gradient(90deg,#d8c1a8,#bfe0e6)" role="img" aria-label="Swimwear banner with model"></div>
  <div class="tile ph" style="left:453px;top:221px;width:290px;height:42px;background:linear-gradient(90deg,#c9ced2,#a8c7d6)" role="img" aria-label="Swim collection banner with model"></div>
  <div class="abs" style="left:460px;top:226px;font-size:16px;color:#333">Selva Marin</div>
  <div class="tile ph" style="left:150px;top:267px;width:593px;height:43px;background:linear-gradient(90deg,#8fd0e4,#4fb7d9 50%,#b9e3ee)" role="img" aria-label="Summer is coming beach banner"></div>
  <div class="tile ph" style="left:756px;top:221px;width:290px;height:89px;background:linear-gradient(135deg,#e47aa0,#f2d9c4 45%,#8fb9d6)" role="img" aria-label="Colourful bikinis fabric banner"></div>

  <div class="abs tab" style="left:150px;top:316px">Latest</div>
  <div class="abs pager" style="left:1014px;top:318px"><i></i><i></i></div>

  <div class="card" style="left:150px;top:330px;height:107px"><div class="img ph" style="background:linear-gradient(#9cc8da,#d9b596)" role="img" aria-label="Model in yellow bikini"></div><div class="meta"><span class="stars">★★★★★</span>Based on 1 reviews.<div class="price">$100.00</div><div class="desc">Lorem ipsum is simply dummy text of<br>the printing...</div></div></div>
  <div class="card" style="left:378px;top:330px;height:107px"><div class="img ph" style="background:linear-gradient(#d4a88c,#c98b72)" role="img" aria-label="Red and polka dot bikini bottoms"></div><div class="meta"><span class="stars">★★★★★</span>Based on 1 reviews.<div class="price">$100.00</div><div class="desc">Lorem ipsum is simply dummy text of<br>the printing...</div></div></div>
  <div class="card" style="left:606px;top:330px;height:107px"><div class="img ph" style="background:linear-gradient(#6fa7d2,#c9a386)" role="img" aria-label="Model in patterned bikini"></div><span class="ribbon"></span><div class="meta"><span class="stars">★★★★★</span>Based on 1 reviews.<div class="price">$100.00</div><div class="desc">Lorem ipsum is simply dummy text of<br>the printing...</div></div></div>
  <div class="card" style="left:832px;top:330px;height:107px"><div class="img ph" style="background:linear-gradient(#7ab2c4,#c49279)" role="img" aria-label="Model in pink bikini"></div><div class="meta"><span class="stars">★★★★★</span>Based on 1 reviews.<div class="price">$100.00</div><div class="desc">Lorem ipsum is simply dummy text of<br>the printing...</div></div></div>

  <div class="abs promo ph" role="img" aria-label="Luxury watch advertisement"></div>
  <div class="abs promo-name">VANTOR WATCHES</div>
  <div class="abs promo-sub">SED DO EIUSMOD TEMPOR INCIDIDUNT</div>

  <aside class="abs cats">
    <div class="cats-head">Categories</div>
    <ul>
      <li style="padding-left:10px">Test Category (0)</li>
      <li>Lorem Ipsum</li><li>Lorem Ipsum</li>
      <li class="plus">Lorem Ipsum</li><li class="plus">Lorem Ipsum</li><li class="plus" style="border:0">Lorem Ipsum</li>
    </ul>
  </aside>
  <div class="abs side-banner ph" role="img" aria-label="Model in black lace bikini"></div>
  <div class="abs side-title wide">LOREM IPSUM</div>
  <div class="abs side-sub wide">dummy text</div>

  <div class="abs tab" style="left:378px;top:482px">Featured</div>
  <div class="abs pager" style="left:1014px;top:484px"><i></i><i></i></div>

  <div class="card" style="left:378px;top:497px;height:106px"><div class="img ph" style="height:68px;background:linear-gradient(#f7f1ea,#e3c3a6)" role="img" aria-label="Model in tan bikini"></div><span class="ribbon"></span><div class="meta"><span class="stars">★★★★★</span>Based on 1 reviews.<div class="price">$107.75<s>$21.50</s></div><div class="desc">Lorem ipsum is simply dummy text of<br>the printing...</div></div></div>
  <div class="card" style="left:604px;top:497px;height:106px"><div class="img ph" style="height:68px;background:linear-gradient(#f8eee6,#eba97c)" role="img" aria-label="Model in orange bikini"></div><div class="meta"><span class="stars">★★★★★</span>Based on 1 reviews.<div class="price">$67.00</div><div class="desc">Lorem ipsum is simply dummy text of<br>the printing...</div></div></div>
  <div class="card" style="left:831px;top:497px;height:106px"><div class="img ph" style="height:68px;background:linear-gradient(#f8f0f1,#dfa9b2)" role="img" aria-label="Model in floral bikini"></div><div class="meta"><span class="stars">★★★★★</span>Based on 1 reviews.<div class="price">$295.75</div><div class="desc">Lorem ipsum is simply dummy text of<br>the printing...</div></div></div>
  <div class="card" style="left:378px;top:609px;height:106px"><div class="img ph" style="height:68px;background:linear-gradient(#f3ede7,#dcc8b4)" role="img" aria-label="Model in white top"></div><span class="ribbon"></span><div class="meta"><span class="stars">★★★★★</span>Based on 1 reviews.<div class="price">$107.75<s>$125.50</s></div><div class="desc">Lorem ipsum is simply dummy text of<br>the printing...</div></div></div>
  <div class="card" style="left:604px;top:609px;height:106px"><div class="img ph" style="height:68px;background:linear-gradient(#f4f5f7,#d6d9de)" role="img" aria-label="Model in white tank top"></div><span class="ribbon"></span><div class="meta"><span class="stars">★★★★★</span>Based on 1 reviews.<div class="price">$107.75<s>$119.50</s></div><div class="desc">Lorem ipsum is simply dummy text of<br>the printing...</div></div></div>
  <div class="card" style="left:831px;top:609px;height:106px"><div class="img ph" style="height:68px;background:linear-gradient(#f6eeea,#d6ad98)" role="img" aria-label="Model in printed bikini"></div><div class="meta"><span class="stars">★★★★★</span>Based on 1 reviews.<div class="price">$49.00</div><div class="desc">Lorem ipsum is simply dummy text of<br>the printing...</div></div></div>

  <div class="abs wide-banner ph" role="img" aria-label="Beach banner with models in bikinis"></div>
  <div class="abs wide-title wide">LOREM IPSUM</div>
  <div class="abs wide-sub wide">dummy text of the printing and typesetting industry.</div>

  <section class="abs services">
    <div class="service"><i style="background:#2e9fe0"></i><div><b style="color:var(--coral)">EASY EXTENDED</b><span>Lorem Ipsum is simply dummy<br>text of the printing...</span></div></div>
    <div class="service"><i style="background:#f07a4a"></i><div><b style="color:var(--coral)">UPTO 5% REWARD</b><span>Lorem Ipsum is simply dummy<br>text of the printing...</span></div></div>
    <div class="service"><i style="background:#e8456b"></i><div><b style="color:var(--green)">DISCOUNTS</b><span>Lorem Ipsum is simply dummy<br>text of the printing...</span></div></div>
    <div class="service"><i style="background:#3cc08a"></i><div><b style="color:#3cc08a">SUPPORT</b><span>Lorem Ipsum is simply dummy<br>text of the printing...</span></div></div>
  </section>
</main>

<footer>
  <div class="abs footer"></div>
  <div class="fcol" style="left:167px;top:815px;width:190px">
    <h4>About Us</h4>
    <div class="ph" style="width:186px;height:20px;background:linear-gradient(90deg,#6fb7d6,#e0c6a6)" role="img" aria-label="Beach photo of a model"></div>
    <div style="margin-top:4px">Lorem Ipsum is simply dummy text of the<br>printing and typesetting industry.</div>
    <div class="fline"><i></i>Phone: +000 0123 555 010</div>
    <div class="fline"><i></i>hello@lorvaneswim.example</div>
  </div>
  <div class="fcol" style="left:386px;top:815px;width:200px">
    <h4>My Twitter</h4>
    <div class="tweet"><i></i><div>Quillform Themes &nbsp; 1d<br>Lorem Ipsum is simply dummy text of the<br><em>Lorem ipsum is simply dummy text of the printing...</em></div></div>
    <div class="tweet"><i></i><div>Quillform Themes &nbsp; 2d<br>Check out this great <em>#swimwear</em> item: New<br>Summer Store Responsive Theme</div></div>
  </div>
  <div class="fcol" style="left:605px;top:815px;width:200px">
    <h4>Latest Blog</h4>
    <div class="blog"><i></i><div><em>LOREM IPSUM IS SIMPLY DUMMY</em><br>Lorem Ipsum is simply dummy text<br>of the printing and typesetting.</div></div>
    <div class="blog"><i></i><div><em>LOREM IPSUM IS SIMPLY DUMMY</em><br>Lorem Ipsum is simply dummy text<br>of the printing and typesetting.</div></div>
    <div class="blog"><i></i><div><em>LOREM IPSUM IS SIMPLY DUMMY</em><br>Lorem Ipsum is simply dummy text.</div></div>
  </div>
  <div class="fcol" style="left:824px;top:815px;width:210px">
    <h4>Newsletter</h4>
    <div>Get our newsletter with weekly offers</div>
    <div style="display:flex;margin-top:3px"><div class="email">Your email address</div><div class="subscribe">Subscribe</div></div>
    <h4 style="margin-top:8px;margin-bottom:1px">Follow us</h4>
    <div>Lorem Ipsum, libero et luctus molestie<br>scelerisque leo.</div>
    <div class="social"><i></i><i></i><i></i><i></i></div>
  </div>

  <div class="fcol" style="left:167px;top:912px"><h4>Information</h4>About Us<br>Delivery Information<br>Privacy Policy<br>Terms &amp; Conditions</div>
  <div class="fcol" style="left:313px;top:912px"><h4>Extras</h4>Brands<br>Gift Vouchers<br>Affiliates<br>Specials</div>
  <div class="fcol" style="left:459px;top:912px"><h4>My Account</h4>My Account<br>Order History<br>Wish List<br>Newsletter</div>
  <div class="fcol" style="left:605px;top:912px"><h4>Customer Service</h4>Contact Us<br>Returns<br>Site Map</div>
  <div class="fcol" style="left:751px;top:912px"><h4>Our Offers</h4>Pricing Policy<br>Shipping Policy<br>Payment Methods<br>Site Information</div>
  <div class="fcol" style="left:897px;top:912px"><h4>Assistance</h4>Shipping &amp; returns<br>Secure shopping<br>My Wishlist<br>Check out</div>

  <div class="abs bottom">
    Powered By <em>ShopFrame</em><br>Quillform Themes © 2014, Designed by <em>Quillform Themes</em>
    <div class="abs pay"><span>Paynet</span><span style="color:#e8734a">Cardo</span><span>Swiftpay</span></div>
  </div>
</footer>
</body>
</html>
```